Business card design for a dynamic IT consulting company

We need a business card design for a young firm, specialized in the Telecommunications/Consulting industry. The name of the company is Dulmar and Partners Business Consulting Ltd. (Short name: Dulmar and Partnes)
Dulmar = solve read reverse, so we aim to be uncomplicated and solution-oriented. The small pipe in our logo is also related to the word solve. So we need a new business card design, which is simple, eye catching and something non traditional (I would probably prefer a square shaped design rather than a rectangle, but open for suggestions). Attached our logo.

Target Market(s)

Usually our customers are Tier1 Telecoms providers (Q-Linkor, Teravine, etc) and their executives.

Industry/Entity Type

Business

Contact Information for Business Card

Name: Gergely Tarnavedi
Email: g.tarnavedi@dulmar-example.hu
Web: www.dulmar-example.hu
Mobile: +36 30 555 0192
Title: Managing Director

Optional:
Company name: Dulmar and Partners Ltd.
Address: 1021 Budapest, Kovarhegyi str. 17/B, Hungary

Font styles to use
Other font styles liked:
• helveticaneue_medium, Prime Regular are used now.

Colors

Designer to choose colors to be used in the design.

Requirements
Must have
• I would like to have a 2 sided design.
Nice to have
• I thought if we make the logo a bit bigger (without the company name), that could go to the back with the company name below. I though, if the pipe in the logo is somehow touchable on the business card, would be nice and unique.

```html
<!DOCTYPE html>
<html lang="en">
<head>
<meta charset="UTF-8">
<title>Dulmar and Partners – Business Card</title>
<link rel="stylesheet" href="https://fonts.googleapis.com/css2?family=Exo+2:wght@400&family=Ubuntu:wght@400&display=swap">
<style>
  :root {
    --stage-top: #2b2b2b;
    --stage-bottom: #161616;
    --card: #262626;
    --card-edge: #1f1f1f;
    --accent-blue: #1596d8;
    --accent-magenta: #b2349a;
    --text-light: #e9e9e9;
    --text-muted: #8a8a8a;
  }
  * { box-sizing: border-box; margin: 0; padding: 0; }
  html, body { width: 1200px; height: 900px; overflow: hidden; }
  body {
    background: radial-gradient(ellipse at 60% 40%, var(--stage-top), var(--stage-bottom) 75%);
    font-family: "Ubuntu", sans-serif;
  }
  .canvas {
    position: relative;
    width: 1200px;
    height: 900px;
    display: flex;
    flex-direction: column;
    align-items: center;
    justify-content: center;
    gap: 48px;
  }
  .card {
    position: relative;
    width: 640px;
    height: 366px;
    background: linear-gradient(135deg, var(--card-edge), var(--card) 55%, #2e2e2e);
    box-shadow: 0 18px 40px rgba(0,0,0,0.55);
    overflow: hidden;
  }
  .card::after {
    content: "";
    position: absolute;
    left: 0; right: 0; bottom: 0;
    height: 6px;
    background: var(--accent-blue);
  }

  /* Front side */
  .card--front {
    display: flex;
    align-items: center;
    justify-content: center;
  }
  .brand {
    display: flex;
    align-items: center;
    gap: 14px;
  }
  .brand__square {
    width: 18px;
    height: 18px;
    background: var(--accent-blue);
  }
  .brand__name {
    font-size: 34px;
    color: var(--text-muted);
    letter-spacing: 0.5px;
  }

  /* Back side */
  .card--back {
    display: flex;
    align-items: center;
    padding: 0 0 20px 0;
  }
  .identity {
    width: 290px;
    text-align: right;
    padding-right: 24px;
  }
  .identity__name {
    font-family: "Exo 2", sans-serif;
    font-size: 25px;
    color: var(--accent-blue);
    text-transform: uppercase;
    letter-spacing: 1px;
    white-space: nowrap;
  }
  .identity__title {
    margin-top: 6px;
    font-size: 16px;
    color: var(--text-light);
    letter-spacing: 0.5px;
  }
  .divider {
    width: 2px;
    height: 64px;
    background: var(--accent-magenta);
  }
  .contact {
    list-style: none;
    padding-left: 24px;
  }
  .contact__item {
    display: flex;
    align-items: center;
    gap: 12px;
    font-size: 15px;
    color: var(--text-light);
    letter-spacing: 0.4px;
    line-height: 24px;
  }
  .contact__icon {
    width: 15px;
    height: 15px;
    flex: none;
  }
</style>
</head>
<body>
  <main class="canvas">
    <section class="card card--front" aria-label="Card front">
      <div class="brand">
        <span class="brand__square"></span>
        <span class="brand__name">Dulmar &amp; Partners</span>
      </div>
    </section>

    <section class="card card--back" aria-label="Card back">
      <div class="identity">
        <p class="identity__name">Gergely Tarnavedi</p>
        <p class="identity__title">Managing Director</p>
      </div>
      <span class="divider"></span>
      <ul class="contact">
        <li class="contact__item">
          <svg class="contact__icon" viewBox="0 0 24 24" aria-hidden="true">
            <path fill="var(--accent-blue)" d="M6.6 10.8a15.1 15.1 0 0 0 6.6 6.6l2.2-2.2a1 1 0 0 1 1-.25 11.4 11.4 0 0 0 3.6.57 1 1 0 0 1 1 1V20a1 1 0 0 1-1 1A17 17 0 0 1 3 4a1 1 0 0 1 1-1h3.5a1 1 0 0 1 1 1c0 1.25.2 2.45.57 3.57a1 1 0 0 1-.25 1z"/>
          </svg>
          +36 30 555 0192
        </li>
        <li class="contact__item">
          <svg class="contact__icon" viewBox="0 0 24 24" aria-hidden="true">
            <rect x="2" y="5" width="20" height="14" rx="1" fill="var(--accent-blue)"/>
            <path d="M2.5 6l9.5 7 9.5-7" fill="none" stroke="var(--card)" stroke-width="1.6"/>
          </svg>
          g.tarnavedi@dulmar-example.hu
        </li>
        <li class="contact__item">
          <svg class="contact__icon" viewBox="0 0 24 24" aria-hidden="true">
            <g fill="none" stroke="var(--accent-blue)" stroke-width="1.8">
              <circle cx="12" cy="12" r="9.5"/>
              <ellipse cx="12" cy="12" rx="4.2" ry="9.5"/>
              <path d="M2.5 12h19M4 7h16M4 17h16"/>
            </g>
          </svg>
          www.dulmar-example.hu
        </li>
      </ul>
    </section>
  </main>
</body>
</html>
```